Looking for a Pagelit Book Cover

My book has been online for a while and I am now looking for a professional cover for it as it has been very well received.

You can view the book here and all the details about it:

https://www.brevolio.example/item/Q7K2WPLTRX#reviews

Not sure what I am looking for as a design, just open to your ideas.

I want something different that will stand out please.

Thanks
Owen

```html
<!DOCTYPE html>
<html lang="en">
<head>
<meta charset="utf-8">
<title>Roots and Resilience — Book Cover</title>
<link rel="stylesheet" href="https://fonts.googleapis.com/css2?family=Anton&family=Roboto+Condensed:wght@400;700&display=swap">
<style>
  :root {
    --backdrop: #5b5b5b;
    --photo-warm: #4a2a22;
    --photo-mid: #2e1f1c;
    --photo-cool: #1c2a30;
    --ink-white: #ffffff;
    --accent-red: #e3202b;
    --band-dark: #221d1e;
  }
  html, body {
    margin: 0;
    width: 1200px;
    height: 1200px;
    overflow: hidden;
    background: var(--backdrop);
  }
  .book-cover {
    position: absolute;
    left: 200px;
    top: 0;
    width: 801px;
    height: 1200px;
    overflow: hidden;
  }
  .cover-photo {
    position: absolute;
    inset: 0;
    background:
      radial-gradient(ellipse 55% 40% at 35% 35%, rgba(120, 70, 55, 0.55), transparent 70%),
      radial-gradient(ellipse 40% 30% at 20% 75%, rgba(100, 55, 45, 0.45), transparent 70%),
      linear-gradient(90deg, var(--photo-warm) 0%, var(--photo-mid) 55%, var(--photo-cool) 100%);
  }
  .cover-type {
    position: absolute;
    inset: 0;
    width: 801px;
    height: 1200px;
  }
  .title-line {
    font-family: "Anton", "Oswald", sans-serif;
    font-size: 213px;
    fill: var(--ink-white);
  }
  .tagline-band { fill: var(--band-dark); }
  .tagline {
    font-family: "Roboto Condensed", "Arial Narrow", sans-serif;
    font-weight: 700;
    font-size: 25px;
    fill: var(--accent-red);
  }
  .subtitle-rule { stroke: var(--accent-red); stroke-width: 2.5; }
  .subtitle {
    font-family: "Roboto Condensed", "Arial Narrow", sans-serif;
    font-weight: 400;
    font-size: 23px;
    fill: var(--ink-white);
  }
  .author-name {
    font-family: "Roboto Condensed", "Arial Narrow", sans-serif;
    font-weight: 700;
    font-size: 69px;
    fill: var(--ink-white);
  }
</style>
</head>
<body>
  <main class="book-cover">
    <div class="cover-photo" role="img" aria-label="Close-up portrait photograph of a Black man's face, one eye looking ahead, skin glistening with sweat against a dark blurred background"></div>

    <svg class="cover-type" viewBox="0 0 801 1200" xmlns="http://www.w3.org/2000/svg">
      <text class="title-line" x="108" y="661" textLength="597" lengthAdjust="spacingAndGlyphs">ROOTS AND</text>

      <text class="title-line" x="108" y="891" textLength="596" lengthAdjust="spacingAndGlyphs">RESILIENCE</text>

      <rect class="tagline-band" x="108" y="669" width="595" height="32"/>
      <text class="tagline" x="124" y="694" textLength="559" lengthAdjust="spacingAndGlyphs">A CELEBRATION OF CULTURE, STRUGGLE AND ACHIEVEMENT</text>

      <line class="subtitle-rule" x1="224" y1="971" x2="224" y2="1036"/>
      <line class="subtitle-rule" x1="612" y1="971" x2="612" y2="1036"/>
      <text class="subtitle" x="243" y="999" textLength="351" lengthAdjust="spacingAndGlyphs">The History, Resistance and Excellence of</text>
      <text class="subtitle" x="243" y="1026" textLength="350" lengthAdjust="spacingAndGlyphs">Black People in Africa and the Diaspora</text>

      <text class="author-name" x="108" y="1155" textLength="595" lengthAdjust="spacingAndGlyphs">DESMOND HARROW</text>
    </svg>
  </main>
</body>
</html>
```